Accommodation business card design

We need a business card designed for our long-term accommodation business based in Australia. The business card must match the style of the attached letterhead and logo. The same contact details that are on the letterhead will also go on the card except that the card must list the contact details in the following order:phone, email, home address, ABN.

The card will be printed on .76mm white pvc plastic (same as credit cards), printed both sides and will be silver foil stamped on at least one side (preferably 2 sides) The design template is attached, but please go to www.zt.com.au for more specs.

The only other addition the card will be my name: Malcolm Darby

```html
<!DOCTYPE html>
<html lang="en">
<head>
<meta charset="utf-8">
<title>Ridgeline Accommodation – Business Card</title>
<link href="https://fonts.googleapis.com/css2?family=Lato:wght@400;700;900&display=swap" rel="stylesheet">
<style>
  :root{
    --maroon:#6b1a3b;
    --maroon-mid:#93526b;
    --maroon-light:#b88a9c;
    --brand-brown:#80433f;
    --ink:#3a2a2e;
    --paper:#ffffff;
    --backdrop:#ecebe7;
  }
  *{margin:0;padding:0;box-sizing:border-box}
  html,body{width:1200px;height:1000px;overflow:hidden}
  body{background:var(--backdrop);font-family:'Lato',sans-serif;position:relative}
  .card{position:absolute;width:628px;height:362px;overflow:hidden;box-shadow:0 3px 8px rgba(0,0,0,.18)}
  .card-back{left:469px;top:499px;background:var(--maroon)}
  .card-front{left:100px;top:172px;background:var(--paper);z-index:2}
  .card-waves{position:absolute;inset:0}
  .brand{position:absolute;left:30px;top:27px;display:flex;align-items:center;gap:14px}
  .brand-square{width:80px;height:84px;border-radius:10px;background:var(--brand-brown)}
  .brand-name{color:var(--brand-brown);font-weight:900;text-transform:uppercase;line-height:.95}
  .brand-name .line-1{display:block;font-size:42px;letter-spacing:1px}
  .brand-name .line-2{display:block;font-size:21px;letter-spacing:.3px}
  .holder-name{position:absolute;left:76px;top:157px;color:var(--maroon);font-weight:700;font-size:21px;font-variant:small-caps;letter-spacing:.5px}
  .contact-list{position:absolute;left:330px;top:165px;list-style:none;color:var(--ink);font-size:15px}
  .contact-item{display:flex;align-items:center;gap:10px;margin-bottom:6px;line-height:15px}
  .contact-item.multi{align-items:flex-start}
  .contact-icon{width:23px;height:23px;flex:none}
  .contact-item.multi .text{padding-top:2px}
  .contact-abn{padding-left:33px;padding-top:2px}
  .contact-abn b{color:var(--maroon);font-weight:700;margin-right:9px}
  .back-square{position:absolute;left:256px;top:120px;width:114px;height:120px;border-radius:14px;background:var(--paper)}
</style>
</head>
<body>

<section class="card card-back" aria-label="Card back">
  <div class="back-square"></div>
</section>

<section class="card card-front" aria-label="Card front">
  <svg class="card-waves" viewBox="0 0 628 362" aria-hidden="true">
    <path d="M350 0 C420 10 470 40 520 62 C560 78 600 84 628 88 L628 0Z" fill="var(--maroon-light)"/>
    <path d="M380 0 C440 12 485 42 530 62 C568 78 605 82 628 84 L628 0Z" fill="var(--maroon-mid)"/>
    <path d="M410 0 C460 14 500 44 545 62 C580 76 610 80 628 82 L628 0Z" fill="var(--maroon)"/>
    <path d="M0 208 C80 215 150 240 230 275 C320 315 420 350 515 362 L0 362Z" fill="var(--maroon-light)"/>
    <path d="M0 210 C70 220 140 250 215 285 C300 322 390 352 470 362 L0 362Z" fill="var(--maroon-mid)"/>
    <path d="M0 213 C60 226 125 262 195 298 C270 336 350 356 420 362 L0 362Z" fill="var(--maroon)"/>
  </svg>

  <div class="brand">
    <div class="brand-square"></div>
    <div class="brand-name"><span class="line-1">Ridgeline</span><span class="line-2">Accommodation</span></div>
  </div>

  <h1 class="holder-name">Malcolm Darby</h1>

  <ul class="contact-list">
    <li class="contact-item">
      <svg class="contact-icon" viewBox="0 0 24 24" aria-hidden="true"><circle cx="12" cy="12" r="12" fill="var(--maroon)"/><path transform="translate(5 5) scale(.58)" d="M6.62 10.79c1.44 2.83 3.76 5.14 6.59 6.59l2.2-2.2c.27-.27.67-.36 1.02-.24 1.12.37 2.33.57 3.57.57.55 0 1 .45 1 1V20c0 .55-.45 1-1 1-9.39 0-17-7.61-17-17 0-.55.45-1 1-1h3.5c.55 0 1 .45 1 1 0 1.25.2 2.45.57 3.57.11.35.03.74-.25 1.02l-2.2 2.2z" fill="#fff"/></svg>
      <span class="text">0400 555 019</span>
    </li>
    <li class="contact-item">
      <svg class="contact-icon" viewBox="0 0 24 24" aria-hidden="true"><circle cx="12" cy="12" r="12" fill="var(--maroon)"/><rect x="5.5" y="7.5" width="13" height="9" rx="1" fill="none" stroke="#fff" stroke-width="1.5"/><path d="M5.5 8 12 13l6.5-5" fill="none" stroke="#fff" stroke-width="1.5"/></svg>
      <span class="text">malcolm.darby@mailbox.net</span>
    </li>
    <li class="contact-item multi">
      <svg class="contact-icon" viewBox="0 0 24 24" aria-hidden="true"><circle cx="12" cy="12" r="12" fill="var(--maroon)"/><path d="M5 12.5 12 6l7 6.5h-2V18h-3.5v-4h-3v4H7v-5.5Z" fill="#fff"/></svg>
      <span class="text">PO Box 1187, Coral Bay Mail Centre<br>QLD 4700</span>
    </li>
    <li class="contact-item contact-abn"><b>ABN</b>12 345 678 901</li>
  </ul>
</section>

</body>
</html>
```